Warehouse Surplus Flyer

2 Sided Flyer to be used in print and online for short, unadvertised sale to pharmacies for prescription vials. Please feel free to edit wordiness.

Side One:
WE PASS ALONG THE SAVINGS TO YOU
WAREHOUSE SURPLUS UNADVERTISED OFFER
BY INVITATION ONLY TO YOU

We have a acquired a surplus, with our supplier, on ALL AMBER color and ALL with CHILD RESISTANT CAPS and we would like to pass along the savings to you, as we need to make room for other inventory.

Normally these vials sell for over $50 a case! We are going to move these vials at very special pricing.

Very cost-effective, Quality Vials

KTR Supply provides pharmacy vials in the independent pharmacy market and conditioned toner cartridges in pharmacies and several other vertical markets.
Please call us at 888-412-5096 and we will be happy to work with you directly.

ktrsupplyco.com

This is not an advertised sale. Offer Ends September 30, 2013*.

2nd Side:
VIAL SIZE QUANTITY PER CASE CASES AVAILABLE
8 Dram 410 50
10 Dram 360 50
13 Dram 310 500
16 Dram 260 500
20 Dram 270 500
30 Dram 240 500
40 Dram 200 500
60 Dram 140 100

During this offer to move inventory, we are selling these at 30% to 50% off our already discounted rate, based on volume.

Quantities: (*While Supplies Last)
• 1 to 500 cases will be sold at 30% off our discounted price! $28 Per Case
• 501 to 1000 cases will be sold at 40% our discounted price! $25 Per Case
• Over 1000 cases will be sold at 50% our discounted price! $22 Per Case

We also have great pricing on conditioned toner cartridges. You can also view our line of products and prices on www.ktrsupplyco.com.

Please call us at 888-412-5096 and we will be happy to work with you directly. This is not an advertised sale.
Updates

Deadline IS AUGUST 28TH! SEPTEMBER SALE.

Target Market(s)

Independent Pharmacies

Industry/Entity Type

Online

Requirements
Must have
• 3 color or Less front side, 2 Sided Flyer
• Backside can be 1 Color
• Phone Number
• web address
• sales expiration date
Nice to have
• graphic call outs to gain attention

```html
<!DOCTYPE html>
<html lang="en">
<head>
<meta charset="utf-8">
<title>KTR Supply – Warehouse Surplus Offer</title>
<link rel="stylesheet" href="https://fonts.googleapis.com/css2?family=Anton&family=Cinzel:wght@700;900&display=swap">
<style>
  :root {
    --royal-blue: #1b2fd3;
    --badge-yellow: #f8ec2a;
    --headline-yellow: #f4e634;
    --green-light: #eef9e8;
    --green-mid: #9ef27c;
    --green-bright: #35e316;
    --white: #ffffff;
    --amber-light: #e9a457;
    --frame: #1a1a1a;
  }
  * { margin: 0; padding: 0; box-sizing: border-box; }
  html, body { width: 927px; height: 1200px; overflow: hidden; background: var(--white); }
  .flyer {
    position: relative;
    width: 927px; height: 1200px;
    border: 2px solid var(--frame);
    background: linear-gradient(90deg, var(--green-light) 0%, var(--green-mid) 45%, var(--green-bright) 100%);
    font-family: "Cinzel", serif;
    font-variant: small-caps;
    color: var(--royal-blue);
    overflow: hidden;
  }
  .line { display: block; white-space: nowrap; }

  .invite-badge {
    position: absolute; left: 8px; top: 2px;
    width: 240px; height: 240px; border-radius: 50%;
    background: var(--badge-yellow);
    border: 6px solid var(--royal-blue);
  }
  .invite-badge p {
    position: absolute; left: 0; right: 0; top: 62px;
    transform: rotate(-27deg);
    text-align: center;
    font-family: "Anton", sans-serif;
    font-variant: normal;
    font-size: 33px; line-height: 1.08; letter-spacing: 0.5px;
    color: var(--royal-blue);
  }
  .headline { position: absolute; left: 0; top: 0; }
  .headline text { font-family: "Anton", sans-serif; fill: var(--royal-blue); }

  .offer-box {
    position: absolute; left: 56px; top: 262px;
    width: 366px; height: 515px;
    background: var(--royal-blue);
    border-radius: 14px;
    color: var(--white);
  }
  .offer-title {
    position: absolute; left: 0; right: 0; top: 30px;
    text-align: center;
    font-size: 25px; font-weight: 900; line-height: 32px; letter-spacing: 0.6px;
    color: var(--headline-yellow);
  }
  .offer-body {
    position: absolute; left: 5px; top: 116px;
    font-size: 20px; font-weight: 900; line-height: 25.5px; letter-spacing: 0.3px;
  }
  .offer-price {
    position: absolute; left: 5px; top: 327px;
    font-size: 26px; font-weight: 900; line-height: 33px; letter-spacing: 0.6px;
  }
  .offer-price .accent { color: var(--headline-yellow); }
  .offer-close {
    position: absolute; left: 5px; top: 444px;
    font-size: 20px; font-weight: 900; line-height: 26px; letter-spacing: 0.3px;
  }

  .product-photo { position: absolute; left: 448px; top: 281px; }
  .mortar-illustration { position: absolute; left: 528px; top: 700px; }

  .brand-box {
    position: absolute; left: 128px; top: 788px;
    width: 243px; height: 259px;
    background: var(--white);
    border: 4px solid var(--royal-blue);
    display: flex; align-items: flex-end; justify-content: center;
    padding-bottom: 16px; gap: 8px;
  }
  .brand-mark { width: 16px; height: 16px; border-radius: 50%; background: var(--royal-blue); margin-bottom: 10px; }
  .brand-name { font-weight: 900; font-size: 30px; font-variant: normal; color: var(--royal-blue); }
  .brand-url {
    position: absolute; left: 118px; top: 1056px; width: 263px;
    text-align: center; font-size: 19px; font-weight: 900; letter-spacing: 0.6px; font-variant: normal;
  }
  .company-about {
    position: absolute; left: 433px; top: 952px;
    font-size: 19px; font-weight: 900; line-height: 25.5px; letter-spacing: 0.4px;
  }
  .contact-line {
    position: absolute; left: 60px; top: 1094px;
    font-size: 19.5px; font-weight: 900; line-height: 25.5px; letter-spacing: 0.5px;
  }
</style>
</head>
<body>
<main class="flyer">
  <svg class="headline" width="927" height="200" viewBox="0 0 927 200">
    <text x="255" y="117" font-size="70" textLength="658" lengthAdjust="spacingAndGlyphs">WE PASS ALONG THE SAVINGS TO YOU</text>
    <text x="271" y="185" font-size="40" textLength="600" lengthAdjust="spacingAndGlyphs">WAREHOUSE SURPLUS UNADVERTISED OFFER</text>
  </svg>

  <div class="invite-badge"><p>BY INVITATION<br>ONLY TO YOU!</p></div>

  <section class="offer-box">
    <h2 class="offer-title"><span class="line">Very cost-effective,</span><span class="line">Quality Vials</span></h2>
    <p class="offer-body">
      <span class="line">We have acquired a surplus,</span>
      <span class="line">with our supplier, on ALL</span>
      <span class="line">AMBER color and ALL with</span>
      <span class="line">CHILD RESISTANT CAPS and</span>
      <span class="line">we would like to pass along</span>
      <span class="line">the savings to you, as we</span>
      <span class="line">need to make room for oth-</span>
      <span class="line">er inventory.</span>
    </p>
    <p class="offer-price">
      <span class="line">Normally these vials</span>
      <span class="line">sell for <span class="accent">over $50</span> a</span>
      <span class="line">case!</span>
    </p>
    <p class="offer-close">
      <span class="line">We are going to move these</span>
      <span class="line">vials at very special pricing.</span>
    </p>
  </section>

  <svg class="product-photo" width="416" height="416" viewBox="0 0 416 416" role="img" aria-label="Photo of amber prescription vials with white child resistant caps">
    <defs>
      <radialGradient id="vialTones" cx="50%" cy="55%" r="60%">
        <stop offset="0%" stop-color="var(--amber-light)"/>
        <stop offset="55%" stop-color="#f3dcc2"/>
        <stop offset="100%" stop-color="#ffffff"/>
      </radialGradient>
    </defs>
    <circle cx="208" cy="208" r="204" fill="url(#vialTones)" stroke="var(--royal-blue)" stroke-width="6"/>
  </svg>

  <svg class="mortar-illustration" width="252" height="232" viewBox="0 0 252 232" role="img" aria-label="Illustration of a mortar and pestle">
    <rect x="0" y="0" width="252" height="232" rx="8" fill="var(--royal-blue)" opacity="0.85"/>
  </svg>

  <div class="brand-box">
    <span class="brand-mark"></span>
    <span class="brand-name">KTR Supply</span>
  </div>
  <p class="brand-url">KTRSUPPLYCO.COM</p>

  <p class="company-about">
    <span class="line">KTR Supply provides pharmacy</span>
    <span class="line">vials in the independent pharmacy</span>
    <span class="line">market and conditioned toner</span>
    <span class="line">cartridges in pharmacies and</span>
    <span class="line">several other vertical markets.</span>
  </p>

  <p class="contact-line">
    <span class="line">Please call us at 888-412-5096 and we will be happy to work</span>
    <span class="line">with you directly. Offer Ends September 30, 2013*.</span>
  </p>
</main>
</body>
</html>
```